Business Card Design Project

Cyber Security. Company name is brightHarbor.

Industry/Entity Type

Computer Security

Contact Information for Business Card

Gregory Lindqvist
Founder and Chief Hacker

2370 W. Alder Rd.
Suite 514
Chicago, IL 60482
773.555.0196
gregory.lindqvist@brightharbor.example
www.brightharbor.example

```html
<!DOCTYPE html>
<html lang="en">
<head>
<meta charset="utf-8">
<title>brightHarbor — Business Cards</title>
<link rel="stylesheet" href="https://fonts.googleapis.com/css2?family=Open+Sans:wght@400;600;700&family=Roboto:wght@400;500&display=swap">
<style>
  :root {
    --canvas: #c4b8a2;
    --card-dark: #383e4d;
    --card-light: #ffffff;
    --brand-blue: #5b72b9;
    --ink: #1c1c1c;
    --ink-soft: #ffffff;
    --band-red: #e9553a;
    --band-green: #8fc23f;
    --band-blue: #3a9ad8;
    --band-taupe: #a99a8a;
  }
  * { box-sizing: border-box; margin: 0; padding: 0; }
  html, body { width: 1200px; height: 1000px; overflow: hidden; }
  body {
    background: var(--canvas);
    font-family: "Open Sans", Arial, sans-serif;
    position: relative;
  }
  .card {
    position: absolute;
    top: 350px;
    width: 520px;
    height: 300px;
    border-radius: 22px;
    overflow: hidden;
    box-shadow: 0 10px 28px rgba(0,0,0,0.25);
  }
  /* Back of card */
  .card--back { left: 50px; background: var(--card-dark); }
  .card--back .wordmark {
    position: absolute; left: 110px; top: 92px;
    display: flex; align-items: center; gap: 14px;
  }
  .wordmark__dot {
    width: 34px; height: 34px; border-radius: 50%;
    background: var(--brand-blue);
  }
  .wordmark__name {
    font-weight: 400; font-size: 50px; letter-spacing: -0.5px;
    color: var(--brand-blue); line-height: 1;
  }
  .card--back .wordmark__name { color: #ffffff; }
  .card--back .wordmark__dot { background: #ffffff; }
  .card--back .address {
    position: absolute; left: 30px; bottom: 52px;
    font-family: "Roboto", Arial, sans-serif;
    font-size: 15px; color: var(--ink-soft);
  }
  .color-band {
    position: absolute; left: 0; bottom: 0; width: 100%; height: 20px;
    display: flex;
  }
  .color-band span { flex: 1; }
  .color-band .red { background: var(--band-red); }
  .color-band .green { background: var(--band-green); }
  .color-band .blue { background: var(--band-blue); }
  .color-band .taupe { background: var(--band-taupe); }

  /* Front of card */
  .card--front { left: 630px; background: var(--card-light); }
  .card--front .wordmark {
    position: absolute; left: 32px; top: 34px;
    display: flex; align-items: center; gap: 10px;
  }
  .card--front .wordmark__dot { width: 26px; height: 26px; }
  .card--front .wordmark__name { font-size: 38px; }
  .person { position: absolute; left: 34px; top: 108px; }
  .person__name {
    font-weight: 700; font-size: 22px; color: var(--brand-blue); line-height: 1.15;
  }
  .person__title {
    font-family: "Roboto", Arial, sans-serif;
    font-size: 15px; color: var(--ink); margin-top: 2px;
  }
  .contact {
    position: absolute; left: 34px; top: 184px; list-style: none;
    font-family: "Roboto", Arial, sans-serif; font-size: 15px; color: var(--ink);
  }
  .contact li { display: flex; align-items: center; gap: 10px; height: 24px; }
  .contact svg { width: 13px; height: 13px; fill: var(--brand-blue); flex: none; }
</style>
</head>
<body>

  <section class="card card--back" aria-label="Card back">
    <div class="wordmark">
      <span class="wordmark__dot"></span>
      <span class="wordmark__name">brightHarbor</span>
    </div>
    <p class="address">2370 W. Alder Rd., Suite 514, Chicago, IL 60482</p>
    <div class="color-band">
      <span class="red"></span><span class="green"></span><span class="blue"></span><span class="taupe"></span>
    </div>
  </section>

  <section class="card card--front" aria-label="Card front">
    <div class="wordmark">
      <span class="wordmark__dot"></span>
      <span class="wordmark__name">brightHarbor</span>
    </div>
    <div class="person">
      <h1 class="person__name">Gregory Lindqvist</h1>
      <p class="person__title">Founder and Chief Hacker</p>
    </div>
    <ul class="contact">
      <li>
        <svg viewBox="0 0 24 24" aria-hidden="true"><path d="M6.6 10.8a15.1 15.1 0 0 0 6.6 6.6l2.2-2.2a1 1 0 0 1 1-.25 11.4 11.4 0 0 0 3.6.57 1 1 0 0 1 1 1V20a1 1 0 0 1-1 1A17 17 0 0 1 3 4a1 1 0 0 1 1-1h3.5a1 1 0 0 1 1 1c0 1.25.2 2.45.57 3.57a1 1 0 0 1-.25 1z"/></svg>
        773.555.0196
      </li>
      <li>
        <svg viewBox="0 0 24 24" aria-hidden="true"><path d="M2 5h20v2l-10 6L2 7z M2 9l10 6 10-6v10H2z"/></svg>
        gregory.lindqvist@brightharbor.example
      </li>
      <li>
        <svg viewBox="0 0 24 24" aria-hidden="true"><path d="M12 2a10 10 0 1 0 0 20 10 10 0 0 0 0-20zm6.9 9h-3a15 15 0 0 0-1.3-6A8 8 0 0 1 18.9 11zM12 4c.9 1.2 1.7 3.8 1.9 7h-3.8c.2-3.2 1-5.8 1.9-7zM9.4 5a15 15 0 0 0-1.3 6h-3A8 8 0 0 1 9.4 5zM5.1 13h3a15 15 0 0 0 1.3 6A8 8 0 0 1 5.1 13zM12 20c-.9-1.2-1.7-3.8-1.9-7h3.8c-.2 3.2-1 5.8-1.9 7zm2.6-1a15 15 0 0 0 1.3-6h3a8 8 0 0 1-4.3 6z"/></svg>
        www.brightharbor.example
      </li>
    </ul>
  </section>

</body>
</html>
```